WP website design (Durham)

We need a wordpress design that will incorporate a professional color scheme with company logo in a clean layout. The design needs to consider that this will be developed on a responsive theme. Colors are undetermined - subdued or subtle, perhaps earth tones colors will likely work well. Logo color can be changed from black to any other to suit.

Client wants a unique look for their site - mentions liking http://www.rvtolan.com/ and http://www.brimscottauction.com/. Possible but not necessary to have large slideshow element.

Industry/Entity Type

It Company

Font styles to use
Serif
Sans Serif

Colors

Designer to choose colors to be used in the design.

Requirements
Must have
• Navigation: 1)Home 2) Auctions 3) For Sale 4) Buyers & Sellers 5) Brokerage 6) About Us 7) Contact Us

Site will have slideshow, please use high-end stock real estate image initially. Header will have logo. Social icons (Facebook, Twitter, Youtube) and tagline "THE REAL ESTATE AUCTION AUTHORITY SINCE 1977" will be used.

Widgets Include: Email signup form, Featured Auctions, News & Events Blog, Featured Video widget.

Footer will have contact info (below), site navigation, smaller company logo, testimonial widget, affiliation logos (attached).
Nice to have
• Site will have drop-down menus - please indicate the styling, for instance the dropdown menus 1) Referrals 2) Properties For Sale under the 'Brokerage' link

```html
<!DOCTYPE html>
<html lang="en">
<head>
<meta charset="utf-8">
<title>Harlow Ridge &amp; Associates — Real Estate Auctions</title>
<link rel="stylesheet" href="https://fonts.googleapis.com/css2?family=Arvo:wght@400;700&family=Montserrat:wght@400;500;600&family=Lora:ital@1&display=swap">
<style>
:root{
  --ink:#222222;
  --panel:#232323;
  --nav:#262626;
  --accent:#c8782c;
  --olive:#908b63;
  --paper:#ffffff;
  --mist:#e6e6e6;
  --footer:#3d3d3d;
  --base:#2a3043;
  --chip:#6f6f6f;
  --link:#1e4f8c;
}
*{box-sizing:border-box;margin:0;padding:0}
html,body{width:1020px;height:1200px;overflow:hidden;background:var(--paper)}
body{font-family:"Montserrat",sans-serif;color:var(--ink)}
.page{position:relative;width:1020px;height:1200px;overflow:hidden}
.abs{position:absolute}

/* header */
.brand{left:107px;top:22px;font-family:"Arvo",serif;font-weight:400;font-size:29px;letter-spacing:-0.5px;color:var(--ink)}
.connect{left:698px;top:36px;font-size:16px;font-weight:500;letter-spacing:.5px}
.social{top:37px;width:17px;height:17px;background:var(--ink);border-radius:3px}

/* navigation */
.nav{left:107px;top:87px;width:806px;height:33px;background:var(--nav);border-radius:4px;display:flex;align-items:center;padding-left:6px;gap:0}
.nav a{color:#fff;text-decoration:none;font-size:13.5px;font-weight:500;margin-right:25px}
.nav a.is-active{color:var(--accent)}
.dropdown{left:459px;top:129px;width:95px;height:60px;background:rgba(60,60,60,.85);border-radius:2px;padding:6px 7px}
.dropdown::before{content:"";position:absolute;left:17px;top:-7px;border:7px solid transparent;border-top:0;border-bottom-color:rgba(170,170,170,.85)}
.dropdown span{display:block;height:11px;margin-bottom:4px;background:#3a3a3a;border:1px solid #999;color:#fff;font-size:6.5px;line-height:9px;padding-left:4px}
.dropdown span.is-hover{background:var(--accent);border-color:var(--accent)}

/* hero */
.hero{left:107px;top:129px;width:806px;height:287px;background:var(--olive);border-radius:3px}
.hero-photo{left:118px;top:140px;width:784px;height:265px;background:linear-gradient(180deg,#a9c3dc 0%,#d6e2ec 45%,#e9e6df 62%,#7d8a64 100%)}
.hero-shadow{left:150px;top:416px;width:720px;height:20px;background:radial-gradient(ellipse at 50% 0,rgba(0,0,0,.22),transparent 70%)}
.signup{left:135px;top:239px;width:276px;height:154px;background:rgba(50,50,50,.85);padding:10px 21px}
.signup h1{font-family:"Arvo",serif;font-weight:700;font-size:15.5px;line-height:19px;color:#fff;text-align:center;letter-spacing:.3px}
.signup p{color:#fff;font-size:9px;line-height:14px;margin-top:11px}
.signup .field{margin-top:4px;height:25px;background:#cfcfcf;border-radius:2px;font-family:"Lora",serif;font-style:italic;font-size:11px;color:#555;padding:6px 12px}
.btn{display:inline-block;background:var(--accent);color:#fff;border-radius:2px}
.signup .btn{margin-top:9px;font-size:10px;font-weight:500;padding:3px 10px}

/* featured auctions */
.auctions{left:106px;top:462px;width:806px;height:260px;background:var(--panel);border-radius:5px 5px 0 0}
.auctions h2{position:absolute;top:19px;width:100%;text-align:center;font-family:"Arvo",serif;font-weight:700;font-size:15px;color:#fff;letter-spacing:.5px}
.arrow{top:554px}
.lot{top:526px;width:125px;text-align:center;color:#fff}
.lot .thumb{width:116px;height:88px;margin:0 auto;border:4px solid #fff;background:linear-gradient(180deg,#86a9cf 0%,#c9b89b 55%,#4e6a3a 100%)}
.lot h3{font-size:12px;font-weight:500;margin-top:8px}
.lot .chips{margin-top:6px;display:flex;justify-content:center;gap:4px}
.lot .chip{background:var(--chip);border:1px solid #999;font-size:6px;padding:3px 4px;color:#fff}
.lot .btn{margin-top:11px;font-size:7.5px;font-weight:500;padding:4px 12px}

/* widgets */
.widgets{left:106px;top:722px;width:806px;height:304px;background:var(--mist)}
.card{top:762px;width:249px;height:218px;background:#fff;border:1px solid #d0d0d0;border-radius:3px}
.card h2{text-align:center;font-family:"Arvo",serif;font-weight:700;font-size:17px;color:#2c2c2c;margin-top:12px}
.card-shadow{top:978px;width:240px;height:12px;background:radial-gradient(ellipse at 50% 0,rgba(0,0,0,.25),transparent 70%)}
.news{position:absolute;left:10px;width:228px;display:flex;gap:6px}
.date{width:31px;flex:none;text-align:center;font-size:11px}
.date .m{background:var(--accent);color:#222;height:18px;line-height:18px;border-radius:2px 2px 0 0}
.date .d{background:var(--base);color:#fff;height:14px;line-height:14px}
.news p{font-size:9px;line-height:14.5px;color:#333}
.news a{color:var(--accent);text-decoration:none}
.divider{position:absolute;left:10px;top:121px;width:227px;border-top:1px solid #ccc}
.video{position:absolute;left:17px;top:60px;width:207px;height:122px;border:3px solid var(--accent);background:linear-gradient(180deg,#5f7fa8 0%,#c7ab87 55%,#3f5a32 90%,#222 100%)}
.quote{position:absolute;left:21px;top:80px;width:210px}
.quote p{font-family:"Lora",serif;font-style:italic;font-size:10px;line-height:13.5px;color:#666;padding-left:30px}
.quote .cite{font-size:11px;text-align:right;margin-top:7px;color:#333;padding-right:20px}
.quote .cite b{font-weight:400;color:var(--link)}
.qnav{position:absolute;top:63px;width:12px;height:12px;background:var(--accent)}

/* footer */
.footer{left:0;top:1026px;width:1020px;height:133px;background:var(--footer)}
.footer-brand{left:111px;top:1063px;width:162px;height:46px;background:#fff;font-family:"Arvo",serif;font-size:17px;color:var(--ink);text-align:center;line-height:46px}
.contact{left:301px;top:1055px;color:#fff}
.contact h2{font-size:15.5px;font-weight:500}
.contact p{font-size:11px;font-weight:500;margin-top:5px;display:flex;align-items:center;gap:7px}
.badge{top:1075px;height:35px;background:#d8d8d8;border-radius:2px}
.basebar{left:0;top:1159px;width:1020px;height:41px;background:var(--base);color:#fff;font-size:9.5px;font-weight:500}
.basebar nav{position:absolute;left:107px;top:15px;display:flex;gap:9px}
.basebar .copy{position:absolute;right:106px;top:15px}
</style>
</head>
<body>
<div class="page">

  <header>
    <div class="abs brand">HARLOW RIDGE</div>
    <div class="abs connect">Connect &nbsp;with Us</div>
    <span class="abs social" style="left:845px" aria-label="Social link 1"></span>
    <span class="abs social" style="left:869px" aria-label="Social link 2"></span>
    <span class="abs social" style="left:893px" aria-label="Social link 3"></span>
  </header>

  <nav class="abs nav">
    <a href="#">Home</a><a href="#">Auctions</a><a href="#">For Sale</a><a href="#">Buyer and Sellers</a><a href="#" class="is-active">Brokerage</a><a href="#">About Us</a><a href="#">Contact Us</a>
  </nav>

  <section>
    <div class="abs hero"></div>
    <div class="abs hero-photo" role="img" aria-label="Photograph of a modern white two-storey house with a dark roof under a blue sky"></div>
    <div class="abs hero-shadow"></div>
    <div class="abs signup">
      <h1>THE REAL ESTATE AUCTION AUTHORITY SINCE 1977</h1>
      <p>Lorem ipsum is a dummy text only. Dolor sit amet, consectetur adipiscing elit.</p>
      <div class="field">Enter Email Address</div>
      <span class="btn">Sign Up Now</span>
    </div>
    <div class="abs dropdown">
      <span class="is-hover">Lorem Ipsum Text</span>
      <span>Lorem Ipsum Text</span>
      <span>Lorem Ipsum Text</span>
    </div>
  </section>

  <section>
    <div class="abs auctions"><h2>FEATURED AUCTIONS</h2></div>
    <svg class="abs arrow" style="left:132px" width="38" height="38" viewBox="0 0 38 38"><circle cx="19" cy="19" r="19" fill="#7a4a22"/><path d="M22 10 L13 19 L22 28" fill="none" stroke="#222" stroke-width="5"/></svg>
    <svg class="abs arrow" style="left:847px" width="38" height="38" viewBox="0 0 38 38"><circle cx="19" cy="19" r="19" fill="#7a4a22"/><path d="M16 10 L25 19 L16 28" fill="none" stroke="#222" stroke-width="5"/></svg>

    <div class="abs lot" style="left:225px"><div class="thumb" role="img" aria-label="Photo of a grey two-storey home with a garage"></div><h3>Pellentesque acsan</h3><div class="chips"><span class="chip">View Details</span><span class="chip">View Gallery</span></div><span class="btn">Click to bid online</span></div>
    <div class="abs lot" style="left:373px"><div class="thumb" role="img" aria-label="Photo of a white colonial home with a porch"></div><h3>Pellentesque acsan</h3><div class="chips"><span class="chip">View Details</span><span class="chip">View Gallery</span></div><span class="btn">Click to bid online</span></div>
    <div class="abs lot" style="left:521px"><div class="thumb" role="img" aria-label="Photo of a yellow house with a front porch"></div><h3>Pellentesque acsan</h3><div class="chips"><span class="chip">View Details</span><span class="chip">View Gallery</span></div><span class="btn">Click to bid online</span></div>
    <div class="abs lot" style="left:669px"><div class="thumb" role="img" aria-label="Photo of a large brick family home"></div><h3>Pellentesque acsan</h3><div class="chips"><span class="chip">View Details</span><span class="chip">View Gallery</span></div><span class="btn">Click to bid online</span></div>
  </section>

  <section>
    <div class="abs widgets"></div>

    <article class="abs card" style="left:117px">
      <h2>Latest News &amp; Events</h2>
      <div class="news" style="top:63px"><div class="date"><div class="m">Sep</div><div class="d">26</div></div><p>Lorem ipsum is a dummy text only. Dolor sit amet, consectetur adipiscing elit. Nullam felis mauris....<a href="#">[Read more]</a></p></div>
      <div class="divider"></div>
      <div class="news" style="top:142px"><div class="date"><div class="m">Sep</div><div class="d">26</div></div><p>Lorem ipsum is a dummy text only. Dolor sit amet, consectetur adipiscing elit. Nullam felis mauris....<a href="#">[Read more]</a></p></div>
    </article>
    <div class="abs card-shadow" style="left:122px"></div>

    <article class="abs card" style="left:385px">
      <h2>Featured Video</h2>
      <div class="video" role="img" aria-label="Video still of a house with a red tiled roof">
        <svg width="201" height="116" viewBox="0 0 201 116">
          <circle cx="100" cy="52" r="27" fill="rgba(0,0,0,.15)" stroke="#fff" stroke-width="3"/>
          <path d="M93 40 L112 52 L93 64 Z" fill="#fff"/>
          <rect x="0" y="104" width="201" height="12" fill="#1a1a1a"/>
          <rect x="22" y="109" width="150" height="2" fill="#555"/>
          <rect x="22" y="109" width="22" height="2" fill="#d33"/>
        </svg>
      </div>
    </article>
    <div class="abs card-shadow" style="left:390px"></div>

    <article class="abs card" style="left:652px">
      <h2>Testimonials</h2>
      <span class="qnav" style="left:184px"></span><span class="qnav" style="left:200px"></span>
      <div class="quote">
        <svg style="position:absolute;left:0;top:0" width="24" height="16" viewBox="0 0 24 16"><path d="M2 16 Q0 6 9 0 L10 3 Q5 6 6 9 L9 9 L9 16 Z M14 16 Q12 6 21 0 L22 3 Q17 6 18 9 L21 9 L21 16 Z" fill="var(--accent)"/></svg>
        <p>Lorem ipsum is a dummy text only. Dolor sit amet, consectetur adipiscing elit. Nullam felis mauris, eleifend ac rhoncus non, lobortis at diam.</p>
        <div class="cite"><b>John Doe</b>, New York</div>
      </div>
    </article>
    <div class="abs card-shadow" style="left:657px"></div>
  </section>

  <footer>
    <div class="abs footer"></div>
    <div class="abs footer-brand">HARLOW RIDGE</div>
    <div class="abs contact">
      <h2>Harlow Ridge &amp; Associates, Inc.</h2>
      <p>1245 Lorem Road, Dummy State 2465</p>
      <p><svg width="16" height="11" viewBox="0 0 16 11"><rect x=".5" y=".5" width="15" height="10" fill="none" stroke="#fff"/><path d="M.5 .5 L8 6 L15.5 .5" fill="none" stroke="#fff"/></svg>Email: contact@harlowridge.example</p>
      <p><svg width="16" height="16" viewBox="0 0 16 16"><circle cx="8" cy="8" r="7.3" fill="none" stroke="#fff"/><path d="M5 4 L6.5 4 L7.2 6 L6.2 7 Q7 9 9 9.8 L10 8.8 L12 9.5 L12 11 Q8 12 5 7 Z" fill="#fff"/></svg>Phone: (555) 014-2297</p>
    </div>
    <span class="abs badge" style="left:665px;width:32px" aria-label="Affiliation badge"></span>
    <span class="abs badge" style="left:705px;width:46px" aria-label="Affiliation badge"></span>
    <span class="abs badge" style="left:759px;width:30px" aria-label="Affiliation badge"></span>
    <span class="abs badge" style="left:797px;width:70px" aria-label="Affiliation badge"></span>
    <span class="abs badge" style="left:871px;width:38px" aria-label="Affiliation badge"></span>

    <div class="abs basebar">
      <nav><span>Home</span><span>Auctions</span><span>For Sale</span><span>Buyer and Sellers</span><span>Brokerage</span><span>About Us</span><span>Contact Us</span></nav>
      <span class="copy">Copyright©Harlow Ridge 2014. All Rights Reserved</span>
    </div>
  </footer>

</div>
</body>
</html>
```